Kai & Palz

I am looking for help designing a concert benefit flyer. I recently designed a ticket for the event. Attached is the font and the back.
The event is being thrown for Kai Bennett Lo'o Lo'o Haver – He is IMAGE 5112 / 5113/5110 ( I have uploaded 3 options – just use the best that you think would work)
We have 7 different artist’s who will be showcased in the event that we would like to incorporate in the flyer
Image 5107 is the main Artist
“ Buro and the list below is his Palz”
Image 5101 is “Pualu”
Image 5102 is Tobin Garcela
Image 5103 is Ikaika Lopes
Image 5104 is Marisa Dutra
Image 5106 is Ilima Segundo
Image 5109 is “Manuheali”
I have uploaded an old flyer we created for a smaller event and was wondering if you could help us design this one ?
Please let me know if you can help and I will go into further details?
Corinne Talua
HALEWAI MANAGEMENT

```html
<!DOCTYPE html>
<html lang="en">
<head>
<meta charset="utf-8">
<title>Buro &amp; Palz – Benefit Concert</title>
<link href="https://fonts.googleapis.com/css2?family=Kaushan+Script&family=Montserrat:wght@700;800;900&family=Open+Sans:wght@700&display=swap" rel="stylesheet">
<style>
  :root {
    --ink: #050302;
    --gold: #f6dc8a;
    --gold-deep: #c98f2c;
    --gold-light: #fff3c9;
    --band: #e9bf62;
    --band-dark: #b88434;
    --white: #ffffff;
  }
  html, body { margin: 0; padding: 0; overflow: hidden; background: #111; }
  .flyer {
    position: relative;
    width: 927px; height: 1200px; overflow: hidden;
    background:
      radial-gradient(ellipse 520px 240px at 50% 930px, rgba(150,60,10,.5), transparent 70%),
      radial-gradient(ellipse 260px 480px at 0% 580px, rgba(110,50,10,.45), transparent 70%),
      radial-gradient(ellipse 260px 480px at 100% 700px, rgba(110,50,10,.4), transparent 70%),
      var(--ink);
    font-family: "Montserrat", sans-serif;
    text-align: center;
  }
  .rays { position: absolute; inset: 0; width: 927px; height: 1200px; }
  .title {
    position: absolute; top: 28px; left: 0; width: 100%; margin: 0;
    font-family: "Kaushan Script", cursive; font-weight: 400;
    font-size: 142px; line-height: 1.1; letter-spacing: 2px;
    background: linear-gradient(180deg, var(--gold-light) 25%, var(--gold-deep) 60%, var(--gold-light) 90%);
    -webkit-background-clip: text; background-clip: text; color: transparent;
  }
  .subtitle {
    position: absolute; top: 212px; left: 0; width: 100%; margin: 0;
    font-family: "Kaushan Script", cursive; font-size: 35px; line-height: 1.35;
    color: var(--white); font-weight: 400;
  }
  .brand-mark {
    position: absolute; left: 410px; top: 372px; width: 128px;
    display: flex; flex-direction: column; align-items: center; gap: 12px;
  }
  .brand-mark .box { width: 72px; height: 72px; border: 3px solid var(--gold-light); }
  .brand-mark .name { font-size: 22px; font-weight: 700; color: var(--gold-light); letter-spacing: 3px; }
  .honoree-photo {
    position: absolute; left: 570px; top: 262px; width: 357px; height: 400px;
    background:
      radial-gradient(ellipse 90px 60px at 62% 16%, #5c6466 0%, #5c6466 70%, transparent 100%),
      radial-gradient(ellipse 100px 110px at 62% 38%, #e2b28f 0%, #d39c7d 70%, transparent 100%),
      radial-gradient(ellipse 200px 150px at 60% 85%, #b8505c 0%, #8c3a44 55%, transparent 100%);
    -webkit-mask-image: radial-gradient(ellipse 62% 58% at 62% 50%, #000 60%, transparent 100%);
    mask-image: radial-gradient(ellipse 62% 58% at 62% 50%, #000 60%, transparent 100%);
  }
  .headline {
    position: absolute; top: 570px; left: 20px; width: 100%; z-index: 2;
    color: var(--gold); font-weight: 800; line-height: 1.15;
  }
  .headline .big { font-size: 33px; letter-spacing: 1.5px; display: block; }
  .headline .byline { font-size: 23px; letter-spacing: 1px; display: block; margin-top: 2px; }
  .headline .byline strong { font-size: 39px; font-weight: 800; letter-spacing: 2px; }
  .headline .raffle { font-size: 24px; letter-spacing: 1.5px; display: block; }
  .artists { position: absolute; top: 780px; left: 0; width: 100%; height: 132px; }
  .artist-photo {
    position: absolute; top: 0; width: 132px; height: 132px; border-radius: 50%;
  }
  .artist-photo.a1 { left: 50px;  background: radial-gradient(circle at 55% 40%, #a27c68, #4c4a4e 55%, #2b2a2e); }
  .artist-photo.a2 { left: 196px; background: linear-gradient(180deg, #f2f0ea 0 20%, #c99a7f 20% 55%, #b5482c 55%); }
  .artist-photo.a3 { left: 335px; background: linear-gradient(180deg, #8a6a48 0 22%, #b08066 22% 58%, #c9403a 58%); }
  .artist-photo.a4 { left: 480px; background: linear-gradient(180deg, #9ab0bc 0 35%, #8c5e4a 35% 60%, #e4dcd2 60%); }
  .artist-photo.a5 { left: 623px; background: linear-gradient(180deg, #d6b27a 0 25%, #3d4a5a 25% 70%, #4f7a3a 70%); }
  .artist-photo.a6 { left: 762px; background: radial-gradient(circle at 50% 45%, #b9876a, #3a3838 60%, #2a2a2c); }
  .feature-band {
    position: absolute; top: 936px; left: 0; width: 100%; height: 86px;
    background: linear-gradient(180deg, var(--band-dark), var(--band) 30%, #f3d48c 60%, var(--band));
    color: var(--ink); font-family: "Open Sans", sans-serif; font-weight: 700;
  }
  .feature-band h2 { margin: 12px 0 4px; font-size: 25px; letter-spacing: 2px; }
  .feature-band p { margin: 0; font-size: 16.5px; letter-spacing: .3px; }
  .event-info {
    position: absolute; top: 1022px; left: 0; width: 100%; height: 178px;
    background: linear-gradient(180deg, #e9c46e, #f2d79a 40%, #d7a44c);
  }
  .event-info .date {
    margin: 14px 0 0; font-size: 37px; font-weight: 900; letter-spacing: 1px; color: var(--ink);
    text-shadow: 2px 0 var(--white), -2px 0 var(--white), 0 2px var(--white), 0 -2px var(--white);
  }
  .event-info .venue {
    margin: 0; font-size: 23px; font-weight: 900; color: var(--ink);
    text-shadow: 1.5px 0 var(--white), -1.5px 0 var(--white), 0 1.5px var(--white), 0 -1.5px var(--white);
  }
  .notice {
    position: absolute; bottom: 20px; left: 0; width: 100%; height: 60px;
    background: rgba(170,120,40,.55);
    font-family: "Open Sans", sans-serif; font-weight: 700; color: var(--ink);
  }
  .notice p { margin: 6px 0 0; font-size: 18px; }
  .notice small { display: block; font-size: 13px; margin-top: 6px; }
</style>
</head>
<body>
<main class="flyer">
  <svg class="rays" viewBox="0 0 927 1200" aria-hidden="true">
    <g stroke="#b45a1a" stroke-width="2" opacity=".45">
      <line x1="0" y1="0" x2="470" y2="930"/>
      <line x1="927" y1="0" x2="460" y2="930"/>
      <line x1="120" y1="0" x2="470" y2="560"/>
      <line x1="800" y1="0" x2="460" y2="560"/>
    </g>
  </svg>

  <h1 class="title">Buro &amp; Palz</h1>
  <p class="subtitle">A Benefit Fundraiser Concert With Dinner<br>For Kai Haver</p>

  <div class="brand-mark">
    <span class="box"></span>
    <span class="name">HAVER</span>
  </div>

  <div class="honoree-photo" role="img" aria-label="Portrait of Kai Haver smiling in a flat cap, floral shirt and lei"></div>

  <div class="headline">
    <span class="big">LIVE HAWAIIAN MUSIC,</span>
    <span class="big">ENTERTAINMENT</span>
    <span class="byline">BY THE <strong>"LANAI LADIES"</strong></span>
    <span class="raffle">AND LIVE RAFFLE GIVEAWAY!</span>
  </div>

  <div class="artists">
    <div class="artist-photo a1" role="img" aria-label="Photo of performer Pualu with a flower in her hair"></div>
    <div class="artist-photo a2" role="img" aria-label="Photo of performer Marisa wearing a white flower crown"></div>
    <div class="artist-photo a3" role="img" aria-label="Photo of performer Tobin in a hat and red plaid shirt"></div>
    <div class="artist-photo a4" role="img" aria-label="Photo of two performers seated with guitars by the water"></div>
    <div class="artist-photo a5" role="img" aria-label="Photo of performer Ilima playing guitar outdoors"></div>
    <div class="artist-photo a6" role="img" aria-label="Photo of performer Ikaika Lopes laughing in a cap"></div>
  </div>

  <section class="feature-band">
    <h2>FEATURING MUSIC BY:</h2>
    <p>BURO - PUALU - MARISA - TOBIN - ILIMA - IKAIKA LOPES - MANUHEALI PRODUCTIONS</p>
  </section>

  <section class="event-info">
    <p class="date">MARCH 9TH, 2024 FROM 4PM - 8PM</p>
    <p class="venue">AT THE CORALVIEW LU'AU PAVILLION</p>
    <div class="notice">
      <p>ALL TICKET SALES WILL GO TOWARDS KAI'S MEDICAL EXPENSES</p>
      <small>*TICKETED ENTRY ONLY</small>
    </div>
  </section>
</main>
</body>
</html>
```